Vantor 7 Rower Vinyl Designs and Vantor Vinyl ArcVane Designs

We would like to have a great design for our Rowers and ArcVanes. The background of the stickers should be dark. Fade or structure is possible. Use our CI Booklet for Fonts, Colors and Logo.

```html
<!DOCTYPE html>
<html lang="en">
<head>
<meta charset="utf-8">
<title>Vantor 7 Rower and ArcVane Stickers</title>
<link rel="stylesheet" href="https://fonts.googleapis.com/css2?family=Archivo:ital,wdth,wght@0,100,800;0,125,600;1,125,900&display=swap">
<style>
  :root {
    --paper: #ffffff;
    --ink: #0d0d0d;
    --navy-deep: #111a2b;
    --navy-glow: #164a73;
    --brand-blue: #164872;
    --slogan-white: #f4f5f7;
    --slogan-grey: #7b7b7b;
    --outline: #121a2a;
  }
  html, body {
    margin: 0;
    padding: 0;
    width: 1200px;
    height: 839px;
    overflow: hidden;
    background: var(--paper);
  }
  .sheet { display: block; width: 1200px; height: 839px; }
  .machine-label {
    font-family: "Archivo", sans-serif;
    font-weight: 800;
    font-size: 84px;
    fill: var(--ink);
    text-anchor: middle;
  }
  .sticker-frame { fill: var(--paper); stroke: var(--outline); stroke-width: 4; }
  .sticker-body { fill: url(#bodyGlow); }
  .slogan {
    font-family: "Archivo", sans-serif;
    font-style: italic;
    font-weight: 900;
    font-stretch: 125%;
    filter: url(#sloganShadow);
  }
  .slogan-top { font-size: 126px; }
  .slogan-main { font-size: 162px; fill: var(--brand-blue); }
  .tone-white { fill: var(--slogan-white); }
  .tone-grey { fill: var(--slogan-grey); }
  .brand-mark { fill: var(--brand-blue); }
  .brand-name {
    font-family: "Archivo", sans-serif;
    font-weight: 600;
    font-stretch: 125%;
    fill: var(--slogan-white);
    font-size: 58px;
  }
</style>
</head>
<body>
<svg class="sheet" viewBox="0 0 2292 1602" xmlns="http://www.w3.org/2000/svg">
  <defs>
    <radialGradient id="bodyGlow" gradientUnits="userSpaceOnUse" cx="588" cy="1360" r="720">
      <stop offset="0" stop-color="var(--navy-glow)"/>
      <stop offset="0.75" stop-color="var(--navy-deep)"/>
    </radialGradient>
    <filter id="sloganShadow" x="-10%" y="-20%" width="120%" height="150%">
      <feDropShadow dx="6" dy="10" stdDeviation="10" flood-color="#000" flood-opacity="0.55"/>
    </filter>
    <path id="shieldOuter" d="M588,383 C800,383 950,435 1050,495 Q1080,515 1082,550 C1092,720 1070,880 990,1040 C900,1210 760,1300 610,1385 Q588,1398 566,1385 C420,1300 280,1210 190,1040 C110,880 85,720 94,550 Q96,515 126,495 C226,435 376,383 588,383Z"/>
    <path id="shieldInner" d="M588,410 C795,410 940,460 1030,518 Q1055,535 1055,570 C1065,730 1040,880 965,1030 C880,1190 745,1285 605,1360 Q588,1370 571,1360 C431,1285 296,1190 211,1030 C136,880 111,730 121,570 Q121,535 146,518 C236,460 381,410 588,410Z"/>
  </defs>

  <!-- Rower sticker -->
  <g class="sticker sticker-rower">
    <text class="machine-label" x="588" y="282">ROWER</text>
    <use href="#shieldOuter" class="sticker-frame"/>
    <use href="#shieldInner" class="sticker-body"/>
    <text class="slogan slogan-top" x="238" y="654" textLength="702" lengthAdjust="spacingAndGlyphs"><tspan class="tone-white">PULL </tspan><tspan class="tone-grey">WITH</tspan></text>
    <text class="slogan slogan-main" x="255" y="799" textLength="657" lengthAdjust="spacingAndGlyphs">POWER</text>
    <circle class="brand-mark" cx="410" cy="985" r="78"/>
    <text class="brand-name" x="522" y="972" textLength="305" lengthAdjust="spacingAndGlyphs">HALDEN</text>
    <text class="brand-name" x="522" y="1050" textLength="305" lengthAdjust="spacingAndGlyphs">STRENGTH</text>
  </g>

  <!-- ArcVane sticker -->
  <g class="sticker sticker-arcvane" transform="translate(1120 0)">
    <text class="machine-label" x="588" y="282">ARCVANE</text>
    <use href="#shieldOuter" class="sticker-frame"/>
    <use href="#shieldInner" class="sticker-body"/>
    <text class="slogan slogan-top" x="206" y="654" textLength="770" lengthAdjust="spacingAndGlyphs"><tspan class="tone-white">EARN </tspan><tspan class="tone-grey">YOUR</tspan></text>
    <text class="slogan slogan-main" x="206" y="799" textLength="765" lengthAdjust="spacingAndGlyphs">METERS</text>
    <circle class="brand-mark" cx="410" cy="985" r="78"/>
    <text class="brand-name" x="522" y="972" textLength="305" lengthAdjust="spacingAndGlyphs">HALDEN</text>
    <text class="brand-name" x="522" y="1050" textLength="305" lengthAdjust="spacingAndGlyphs">STRENGTH</text>
  </g>
</svg>
</body>
</html>
```